Bright Lark Financial
Business cards and stationary
Project: Bright Lark Financial
Bright Lark Financial  - Financial Services
Creative Brief
Modern
Lyn Vorhaus, Planner
Owner/CERTIFIED FINANCIAL PLANNER(tm)
418 Orchard Plaza Court #512 Larkmere Vale, QX 40219
lyn@brightlarkfinancial.example
www.brightlarkfinancial.example
CA Ins #0K48215
1st inside card: this is where you can get creative - "What will you do when your money works for you?" Have visual photos of retirement, playing with grandchildren, sailing, traveling, active lifestyle photos or icons. Inside card: BrightLark Financial supports & educates women in technology through financial planning & investment management outsourcing.
Bright Lark Financial is a part of Vorhaus Financial Group. Registered Representative, Securities offered through Pelham Asset Partners, Inc., a Broker/Dealer, Member QOLMA/TRBX. Investment Advisor Representative, Pelham Asset Partners Advisors, Inc., a Registered Investment Advisor. Pelham and Bright Lark Financial/Vorhaus Financial Group are not affiliated.

```html
<!DOCTYPE html>
<html lang="en">
<head>
<meta charset="utf-8">
<title>Bright Lark Financial – Stationery Options</title>
<link href="https://fonts.googleapis.com/css2?family=Open+Sans:wght@400;600;700&display=swap" rel="stylesheet">
<style>
:root{
  --bg:#ece9e4;
  --paper:#ffffff;
  --navy:#2d2a78;
  --green:#8cc63f;
  --ink:#555a66;
  --rule:#c9ccd3;
  --label:#3a3a3a;
}
*{box-sizing:border-box;margin:0;padding:0}
html,body{width:1200px;height:434px;overflow:hidden}
body{background:var(--bg);font-family:"Open Sans",Arial,sans-serif;color:var(--ink);position:relative}
.sheet{position:absolute;top:88px;width:170px;height:215px;background:var(--paper);box-shadow:0 2px 6px rgba(0,0,0,.25);overflow:hidden}
.brand{position:absolute;left:12px;top:10px;display:flex;align-items:center;gap:4px;font-size:8px;font-weight:600;color:var(--navy);white-space:nowrap}
.brand .dot{width:8px;height:8px;border-radius:50%;background:var(--green)}
.contact{position:absolute;right:10px;top:11px;font-size:3px;line-height:4.2px;text-align:right}
.disclaimer{position:absolute;left:10px;right:10px;bottom:6px;font-size:2.6px;line-height:3.4px;text-align:center}
.wave{position:absolute;left:0;bottom:0;width:170px;height:40px}
.wave-text{position:absolute;right:8px;bottom:5px;font-size:3px;line-height:4px;color:#fff;text-align:right}
.option-label{position:absolute;top:312px;width:170px;text-align:center;font-size:11px;color:var(--label)}
.fax-title{position:absolute;left:10px;top:34px;font-size:9px;font-weight:700;color:var(--label)}
.fax-fields{position:absolute;left:10px;right:12px;top:50px;font-size:3.6px;line-height:5px}
.fax-fields div{border-bottom:0.5px solid var(--rule);padding:1px 0;margin-bottom:2px}
.fax-checks{position:absolute;left:10px;right:10px;top:96px;display:flex;justify-content:space-between;font-size:3.2px;line-height:4px}
.fax-checks span::before{content:"";display:inline-block;width:3px;height:3px;border:0.5px solid var(--ink);margin-right:1px;vertical-align:middle}
.envelope{position:absolute;width:280px;height:108px;background:var(--paper);box-shadow:0 2px 5px rgba(0,0,0,.25);overflow:hidden}
.envelope .brand{left:auto;right:12px;font-size:7px}
.envelope .band{position:absolute;left:0;top:0;width:280px;height:34px}
.card{position:absolute;background:var(--paper);box-shadow:0 1px 4px rgba(0,0,0,.25);overflow:hidden}
.card-caption{position:absolute;font-size:5px;color:var(--label);text-align:center}
.icon-row{position:absolute;left:6px;right:6px;top:12px;display:flex;flex-wrap:wrap;gap:4px;justify-content:center}
.icon-row span{width:14px;height:14px;border-radius:50%;background:radial-gradient(#9aa3b5,#4a5468)}
</style>
</head>
<body>

<section class="sheet" style="left:20px">
  <div class="brand"><span class="dot"></span>brightlark</div>
  <div class="contact">Lyn Vorhaus, Planner<br>418 Orchard Plaza Court #512<br>Larkmere Vale, QX 40219<br>lyn@brightlarkfinancial.example</div>
  <div class="disclaimer">Securities offered through Pelham Asset Partners, Inc., Member QOLMA/TRBX.<br>www.brightlarkfinancial.example · CA Ins #0K48215</div>
</section>
<div class="option-label" style="left:20px">Option-1</div>

<section class="sheet" style="left:225px">
  <div class="brand"><span class="dot"></span>brightlark</div>
  <div class="contact">Lyn Vorhaus, Planner<br>lyn@brightlarkfinancial.example</div>
  <svg class="wave" viewBox="0 0 170 40" aria-hidden="true">
    <path d="M0 16 C55 4 110 30 170 8" fill="none" stroke="var(--green)" stroke-width="2"/>
    <path d="M0 21 C55 9 110 34 170 13 V40 H0Z" fill="var(--navy)"/>
  </svg>
  <div class="wave-text">418 Orchard Plaza Court #512 Larkmere Vale, QX 40219<br>www.brightlarkfinancial.example</div>
</section>
<div class="option-label" style="left:225px">Option-2</div>

<section class="sheet" style="left:430px">
  <div class="brand"><span class="dot"></span>brightlark</div>
  <svg class="wave" viewBox="0 0 170 40" aria-hidden="true">
    <path d="M0 12 C60 30 120 2 170 16" fill="none" stroke="var(--green)" stroke-width="2"/>
    <path d="M0 18 C60 36 120 8 170 22 V40 H0Z" fill="var(--navy)"/>
  </svg>
  <div class="disclaimer" style="bottom:44px;text-align:left">Bright Lark Financial is a part of Vorhaus Financial Group.<br>Securities offered through Pelham Asset Partners, Inc.</div>
  <div class="wave-text">Lyn Vorhaus, Planner · lyn@brightlarkfinancial.example<br>www.brightlarkfinancial.example</div>
</section>
<div class="option-label" style="left:430px">Option-3</div>

<section class="sheet" style="left:635px">
  <div class="brand"><span class="dot"></span>brightlark</div>
  <div class="fax-title">FAX</div>
  <div class="fax-fields"><div>To:</div><div>From:</div><div>Fax:</div><div>Date:</div><div>Re:</div></div>
  <div class="fax-checks"><span>Urgent</span><span>For Review</span><span>Please Comment</span><span>Please Reply</span></div>
  <svg class="wave" viewBox="0 0 170 40" aria-hidden="true">
    <path d="M0 16 C55 4 110 30 170 8" fill="none" stroke="var(--green)" stroke-width="2"/>
    <path d="M0 21 C55 9 110 34 170 13 V40 H0Z" fill="var(--navy)"/>
  </svg>
  <div class="wave-text">www.brightlarkfinancial.example</div>
</section>
<div class="option-label" style="left:635px">Option-4</div>

<section class="envelope" style="left:900px;top:18px">
  <svg class="band" viewBox="0 0 280 34" aria-hidden="true"><path d="M0 0 H280 V8 C180 22 90 2 0 18Z" fill="var(--navy)" opacity=".85"/></svg>
  <div class="brand" style="top:26px"><span class="dot"></span>brightlark</div>
</section>
<section class="envelope" style="left:890px;top:60px">
  <svg class="band" viewBox="0 0 280 34" aria-hidden="true"><path d="M0 0 H280 V8 C180 20 90 4 0 18Z" fill="var(--green)"/></svg>
  <div class="brand" style="top:26px"><span class="dot"></span>brightlark</div>
</section>
<section class="envelope" style="left:880px;top:102px">
  <svg class="band" viewBox="0 0 280 34" aria-hidden="true"><path d="M0 0 L140 30 L280 0" fill="none" stroke="var(--rule)" stroke-width="1"/></svg>
  <div class="brand" style="top:8px"><span class="dot"></span>brightlark</div>
</section>
<section class="envelope" style="left:870px;top:144px;height:80px">
  <div class="brand" style="top:8px"><span class="dot"></span>brightlark</div>
  <svg class="wave" style="width:280px;height:26px" viewBox="0 0 280 26" aria-hidden="true">
    <path d="M0 10 C90 0 190 22 280 4" fill="none" stroke="var(--green)" stroke-width="2"/>
    <path d="M0 14 C90 4 190 26 280 8 V26 H0Z" fill="var(--navy)"/>
  </svg>
</section>

<section class="card" style="left:925px;top:240px;width:46px;height:66px">
  <div class="brand" style="left:5px;top:6px;font-size:5px;gap:2px"><span class="dot" style="width:5px;height:5px"></span>brightlark</div>
  <svg class="wave" style="width:46px;height:14px" viewBox="0 0 46 14" aria-hidden="true"><path d="M0 6 C15 2 30 12 46 3 V14 H0Z" fill="var(--navy)"/></svg>
</section>
<div class="card-caption" style="left:925px;top:310px;width:46px">Front</div>

<section class="card" style="left:1020px;top:240px;width:66px;height:50px">
  <div class="icon-row" role="img" aria-label="Lifestyle photos: retirement, family, sailing, travel"><span></span><span></span><span></span><span></span></div>
</section>
<div class="card-caption" style="left:1020px;top:296px;width:66px">Inside Business</div>

</body>
</html>
```